Business card design needed

I would like a clean simple buisness card as a freelance makeup artist.The main colours i would like are black, white card (grey tones) with a pop of red or purple. Card mostly white. Double sided. Front side featuring a vector graphic plain face chart-similiar to the LUX/Corvin Halloway design. Face can be partially shown/cropped or in full. Some white space near text at the front - "Rel Dosk MUA" then in smaller text underneath "Make me over" then rest of the contact details.Font is walkway font.

Rel Dosk MUA Make me over m: 0431 768 209 e: relmira_dosk@fernpost.example

```html
<!DOCTYPE html>
<html lang="en">
<head>
<meta charset="utf-8">
<title>Rel Dosk MUA – Business Card</title>
<link rel="stylesheet" href="https://fonts.googleapis.com/css2?family=Questrial&display=swap">
<style>
  :root {
    --stage: #ededed;
    --card-dark: #2b2a29;
    --card-light: #ffffff;
    --accent-red: #e3262b;
    --ink-dark: #2b2a29;
    --ink-light: #ffffff;
    --art-dark-a: #3a3938;
    --art-dark-b: #5a5958;
    --art-light-a: #f2f2f2;
    --art-light-b: #d6d6d6;
  }
  * { box-sizing: border-box; margin: 0; padding: 0; }
  html, body {
    width: 1077px;
    height: 1200px;
    overflow: hidden;
    background: var(--stage);
    font-family: "Questrial", "Helvetica Neue", Arial, sans-serif;
  }
  .canvas {
    position: relative;
    width: 1077px;
    height: 1200px;
  }
  .card {
    position: absolute;
    width: 806px;
    height: 448px;
    border-radius: 22px;
    overflow: hidden;
  }
  .card--front { left: 135px; top: 135px; background: var(--card-dark); }
  .card--back  { left: 140px; top: 625px; background: var(--card-light); }

  .card__art {
    position: absolute;
    width: 248px;
    height: 414px;
    border-radius: 6px;
  }
  .card--front .card__art {
    left: 554px; top: 27px;
    background: linear-gradient(160deg, var(--art-dark-b), var(--art-dark-a));
  }
  .card--back .card__art {
    left: 544px; top: 32px;
    background: linear-gradient(160deg, var(--art-light-a), var(--art-light-b));
  }

  .brand-name {
    position: absolute;
    font-size: 34px;
    line-height: 1;
    color: var(--accent-red);
    white-space: nowrap;
  }
  .tagline {
    position: absolute;
    line-height: 1;
    white-space: nowrap;
  }
  .card--front .brand-name { left: 188px; top: 178px; }
  .card--front .tagline { left: 232px; top: 246px; font-size: 21px; color: var(--ink-light); }

  .card--back .brand-name { left: 129px; top: 120px; }
  .card--back .tagline { left: 132px; top: 165px; font-size: 25px; color: var(--ink-dark); }

  .contact-list {
    position: absolute;
    left: 94px;
    top: 236px;
    list-style: none;
  }
  .contact-item {
    display: flex;
    align-items: center;
    height: 46px;
    font-size: 27px;
    color: var(--ink-dark);
    white-space: nowrap;
  }
  .contact-icon {
    width: 28px;
    height: 24px;
    margin-right: 10px;
    flex: none;
  }
</style>
</head>
<body>
<main class="canvas">

  <section class="card card--front" aria-label="Card front">
    <h1 class="brand-name">Rel Dosk MUA</h1>
    <p class="tagline">Make me over</p>
    <div class="card__art" role="img" aria-label="White line-art face chart illustration, partially cropped"></div>
  </section>

  <section class="card card--back" aria-label="Card back">
    <h2 class="brand-name">Rel Dosk MUA</h2>
    <p class="tagline">Make me over</p>
    <ul class="contact-list">
      <li class="contact-item">
        <svg class="contact-icon" viewBox="0 0 28 24" aria-hidden="true">
          <rect x="8" y="2" width="12" height="20" rx="2" fill="none" stroke="var(--accent-red)" stroke-width="1.6"/>
          <line x1="8" y1="17" x2="20" y2="17" stroke="var(--accent-red)" stroke-width="1.4"/>
          <circle cx="14" cy="19.5" r="0.9" fill="var(--accent-red)"/>
        </svg>
        <span>0431 768 209</span>
      </li>
      <li class="contact-item">
        <svg class="contact-icon" viewBox="0 0 28 24" aria-hidden="true">
          <rect x="2" y="5" width="24" height="15" fill="none" stroke="var(--accent-red)" stroke-width="1.6"/>
          <polyline points="2,5 14,14 26,5" fill="none" stroke="var(--accent-red)" stroke-width="1.6"/>
          <line x1="2" y1="20" x2="11" y2="12" stroke="var(--accent-red)" stroke-width="1.4"/>
          <line x1="26" y1="20" x2="17" y2="12" stroke="var(--accent-red)" stroke-width="1.4"/>
        </svg>
        <span>relmira_dosk@fernpost.example</span>
      </li>
    </ul>
    <div class="card__art" role="img" aria-label="Black line-art face chart illustration, partially cropped"></div>
  </section>

</main>
</body>
</html>
```